Sleek business card design for digital agency.

Brief document attached for detailed description and inspiration. Looking for a minimalist sleek, cool, modern business card design.

Industry/Entity Type

Digital

```html
<!DOCTYPE html>
<html lang="en">
<head>
<meta charset="utf-8">
<title>Rivet Works — Business Card</title>
<link href="https://fonts.googleapis.com/css2?family=Open+Sans:wght@400;600;700&display=swap" rel="stylesheet">
<style>
  :root {
    --stage: #2a2520;
    --card: #111111;
    --card-edge: #1c1c1c;
    --gloss: #2c2c2c;
    --white: #f2f2f2;
    --muted: #8d8d8d;
    --accent: #3a9ad9;
    --icon: #3a9ad9;
  }
  * { margin: 0; padding: 0; box-sizing: border-box; }
  html, body {
    width: 1200px; height: 676px; overflow: hidden;
    background: var(--stage);
    font-family: "Open Sans", sans-serif;
  }
  .stage {
    width: 1200px; height: 676px;
    display: flex; align-items: center; justify-content: center; gap: 40px;
  }
  .card {
    width: 520px; height: 297px;
    background: var(--card);
    border: 1px solid var(--card-edge);
    border-radius: 3px;
    position: relative;
    box-shadow: 0 10px 30px rgba(0,0,0,.45);
  }
  /* Front */
  .card--front { display: flex; align-items: center; justify-content: center; }
  .front-wordmark {
    font-size: 58px; font-weight: 700; letter-spacing: 1px;
    color: var(--gloss);
  }
  /* Back */
  .brand {
    position: absolute; top: 40px; right: 44px;
    display: flex; align-items: center; gap: 10px;
    font-size: 15px; font-weight: 600; color: var(--muted);
  }
  .brand-dot { width: 30px; height: 30px; border-radius: 50%; background: #3a3a3a; }
  .details { position: absolute; left: 44px; top: 44px; }
  .name {
    font-size: 21px; font-weight: 700; letter-spacing: 2px;
    color: var(--white); text-transform: uppercase;
  }
  .name .surname { color: var(--accent); }
  .role, .drink, .address { font-size: 12px; color: var(--muted); line-height: 1.55; }
  .role { margin-top: 4px; }
  .address { margin-top: 18px; }
  .contacts { list-style: none; margin-top: 16px; }
  .contacts li {
    display: flex; align-items: center; gap: 9px;
    font-size: 12px; color: var(--muted); line-height: 1.6;
  }
  .contacts svg { width: 10px; height: 10px; flex: none; }
</style>
</head>
<body>
<main class="stage">
  <section class="card card--front">
    <span class="front-wordmark">Rivet Works</span>
  </section>

  <section class="card card--back">
    <div class="brand"><span class="brand-dot"></span>Rivet Works</div>
    <div class="details">
      <h1 class="name">Daniel <span class="surname">Hale</span></h1>
      <p class="role">Marketing Director</p>
      <p class="drink">Drink order: G&amp;T with cucumber</p>
      <p class="address">Level 2, 18 Carden St<br>East Harbour NSW 5000</p>
      <ul class="contacts">
        <li>
          <svg viewBox="0 0 10 10"><path d="M2 0.5 L4 2.8 L3 4 Q4.5 6 6 7 L7.2 6 L9.5 8 L8 9.6 Q3.5 9 0.4 2 Z" fill="var(--icon)"/></svg>
          0400 123 456
        </li>
        <li>
          <svg viewBox="0 0 10 10"><rect x="0.5" y="3" width="9" height="6.5" rx="1" fill="var(--icon)"/><rect x="2" y="0.5" width="6" height="2" rx="1" fill="var(--icon)"/></svg>
          03 9000 1234
        </li>
        <li>
          <svg viewBox="0 0 10 10"><rect x="0.5" y="0.5" width="9" height="9" rx="1.5" fill="var(--icon)"/></svg>
          @dhale82
        </li>
        <li>
          <svg viewBox="0 0 10 10"><rect x="0.5" y="1.5" width="9" height="7" rx="0.8" fill="var(--icon)"/><path d="M0.8 2 L5 5.5 L9.2 2" stroke="var(--card)" stroke-width="0.9" fill="none"/></svg>
          dhale@rivetworks.com
        </li>
        <li>
          <svg viewBox="0 0 10 10"><rect x="0.5" y="0.5" width="9" height="9" rx="1.5" fill="var(--icon)"/></svg>
          social.example/RivetWorks
        </li>
      </ul>
    </div>
  </section>
</main>
</body>
</html>
```